Byaruhanga & Odongo Advocates website

An interactive professional law firm website fully synchronized with social media pages.

Target Market(s)

Corporations and professionals

Industry/Entity Type

Professional Service

Number of Pages Required

5+ page

Font styles to use
Sans Serif

Colors

Designer to choose colors to be used in the design.

```html
<!DOCTYPE html>
<html lang="en">
<head>
<meta charset="utf-8">
<title>Byaruhanga &amp; Odongo Advocates</title>
<link rel="stylesheet" href="https://fonts.googleapis.com/css2?family=Roboto:wght@400;500;700&display=swap">
<style>
  :root {
    --brand: #8c111e;
    --ink: #444;
    --ink-soft: #5a5a5a;
    --line: #e4e4e4;
    --card: #f8f8f8;
    --white: #fff;
  }
  * { box-sizing: border-box; margin: 0; padding: 0; }
  html, body { width: 1200px; height: 1200px; overflow: hidden; background: var(--white); }
  body { position: relative; font-family: 'Roboto', sans-serif; color: var(--ink); }

  .hero {
    position: absolute; left: 0; top: 0; width: 1200px; height: 514px;
    background: linear-gradient(180deg, #cbcadf 0%, #bebdd6 45%, #aeadc2 75%, #979aa3 100%);
  }
  .hero-copy { position: absolute; left: 0; right: 0; top: 284px; text-align: center; color: var(--white); }
  .hero-lead { font-size: 20px; letter-spacing: 1.6px; font-weight: 500; }
  .hero-title { font-size: 26px; font-weight: 700; letter-spacing: 1.4px; margin-top: 4px; }
  .hero-btn {
    position: absolute; left: 538px; top: 378px; width: 140px; height: 42px;
    background: var(--brand); color: var(--white); border-radius: 3px;
    font-size: 15px; font-weight: 700; letter-spacing: 1.2px;
    display: flex; align-items: center; justify-content: center;
  }
  .hero-dots { position: absolute; top: 477px; left: 585px; display: flex; gap: 6px; }
  .hero-dots span { width: 11px; height: 11px; border: 1.5px solid var(--white); border-radius: 50%; }
  .hero-dots span.active { background: var(--brand); }

  .site-header {
    position: absolute; left: 34px; top: 0; width: 1129px; height: 95px;
    background: rgba(255,255,255,.95); display: flex; align-items: center;
  }
  .brand { display: flex; align-items: center; gap: 10px; margin-left: 20px; width: 500px; }
  .brand-mark { width: 14px; height: 14px; background: var(--brand); }
  .brand-name { font-size: 19px; line-height: 21px; color: #555; font-weight: 400; }
  .main-nav { display: flex; height: 95px; margin-left: 20px; }
  .main-nav a {
    display: flex; align-items: center; font-size: 17px; letter-spacing: 1.2px;
    color: #555; text-decoration: none; padding: 0 12px;
  }
  .main-nav a.current { background: var(--brand); color: var(--white); font-weight: 500; padding: 0 16px; margin-right: 4px; }

  .intro {
    position: absolute; left: 175px; width: 850px; top: 593px; text-align: center;
    font-size: 16.5px; line-height: 24px; letter-spacing: 1.1px; color: var(--ink-soft);
  }
  .intro strong { font-weight: 700; color: var(--ink); }

  .stat { position: absolute; top: 727px; height: 112px; display: flex; background: var(--card); border: 1px solid #eee; }
  .stat-icon { width: 99px; height: 112px; background: var(--brand); display: flex; align-items: center; justify-content: center; }
  .stat-body { padding: 20px 0 0 21px; }
  .stat-label { color: var(--brand); font-size: 16.5px; letter-spacing: 1.6px; line-height: 24px; }
  .stat-value { color: #444; font-size: 25px; font-weight: 700; letter-spacing: 1.2px; margin-top: 6px; }
  .stat.single .stat-body { padding-top: 36px; }

  .section-rule { position: absolute; top: 942px; height: 2px; background: var(--line); }
  .section-dot { position: absolute; left: 593px; top: 932px; width: 28px; height: 28px; border-radius: 50%; background: var(--brand); }
  .section-title { position: absolute; left: 0; right: 0; top: 982px; text-align: center; font-size: 21px; font-weight: 400; letter-spacing: 2.4px; color: #555; }
  .section-title strong { color: #333; font-weight: 700; }

  .method-photo { position: absolute; top: 1102px; height: 98px; }
  .method-badge {
    position: absolute; top: 1059px; width: 96px; height: 96px; border-radius: 50%;
    background: var(--brand); border: 8px solid var(--white);
    display: flex; align-items: center; justify-content: center;
  }
</style>
</head>
<body>
  <section class="hero" role="img" aria-label="Long concrete bridge stretching over calm misty water"></section>
  <div class="hero-copy">
    <p class="hero-lead">To provide legal services focused on</p>
    <h1 class="hero-title">Commercial Litigation, Construction Law &amp; Arbitration.</h1>
  </div>
  <a class="hero-btn">KNOW MORE</a>
  <div class="hero-dots"><span></span><span class="active"></span><span></span></div>

  <header class="site-header">
    <div class="brand">
      <span class="brand-mark"></span>
      <span class="brand-name">Byaruhanga &amp; Odongo<br>Advocates</span>
    </div>
    <nav class="main-nav">
      <a class="current">Home</a>
      <a>About Us</a>
      <a>Our Professionals</a>
      <a>Clients</a>
      <a>Contact Us</a>
    </nav>
  </header>

  <p class="intro"><strong>Byaruhanga &amp; Odongo Advocates</strong> are a specialist commercial law firm in Uganda focusing on commercial litigation, construction law and arbitration. We have excelled in our niche areas for over two decades and we continue to grow and be the firm choice in those practice areas.</p>

  <div class="stat single" style="left:33px;width:245px">
    <div class="stat-icon">
      <svg width="58" height="44" viewBox="0 0 58 44" fill="#fff"><circle cx="18" cy="11" r="9"/><circle cx="40" cy="11" r="9"/><path d="M2 44c0-12 7-20 16-20s16 8 16 20z"/><path d="M24 44c0-12 7-20 16-20s16 8 16 20z"/></svg>
    </div>
    <div class="stat-body"><div class="stat-label">PARTNERS</div><div class="stat-value">5</div></div>
  </div>
  <div class="stat single" style="left:306px;width:246px">
    <div class="stat-icon">
      <svg width="58" height="54" viewBox="0 0 58 54" fill="#fff"><circle cx="29" cy="8" r="7"/><circle cx="14" cy="18" r="6"/><circle cx="44" cy="18" r="6"/><circle cx="29" cy="26" r="7"/><path d="M2 44c0-9 5-15 12-15s12 6 12 15z"/><path d="M32 44c0-9 5-15 12-15s12 6 12 15z"/><path d="M14 54c0-11 7-18 15-18s15 7 15 18z"/></svg>
    </div>
    <div class="stat-body"><div class="stat-label">PEOPLE</div><div class="stat-value">20+</div></div>
  </div>
  <div class="stat" style="left:581px;width:311px">
    <div class="stat-icon">
      <svg width="52" height="52" viewBox="0 0 52 52"><rect x="3" y="8" width="46" height="41" fill="none" stroke="#fff" stroke-width="3"/><rect x="3" y="8" width="46" height="8" fill="#fff"/><rect x="13" y="2" width="4" height="10" fill="#fff"/><rect x="35" y="2" width="4" height="10" fill="#fff"/><text x="26" y="42" text-anchor="middle" font-family="Roboto, sans-serif" font-weight="700" font-size="20" fill="#fff">55</text></svg>
    </div>
    <div class="stat-body"><div class="stat-label">YEAR OF COMBINED<br>EXPERIENCE</div><div class="stat-value" style="margin-top:2px">55</div></div>
  </div>
  <div class="stat" style="left:918px;width:245px">
    <div class="stat-icon">
      <svg width="60" height="50" viewBox="0 0 60 50" fill="#fff"><rect x="12" y="32" width="7" height="18"/><rect x="25" y="26" width="7" height="24"/><rect x="38" y="20" width="7" height="30"/><path d="M2 32l16-14 12 10 18-18" fill="none" stroke="#fff" stroke-width="5"/><path d="M42 4h16v16z"/></svg>
    </div>
    <div class="stat-body"><div class="stat-label">CASES<br>SOLVED</div><div class="stat-value" style="margin-top:2px">350+</div></div>
  </div>

  <div class="section-rule" style="left:34px;width:543px"></div>
  <div class="section-rule" style="left:640px;width:522px"></div>
  <div class="section-dot"></div>
  <h2 class="section-title">HOW <strong>WE DO IT</strong></h2>

  <div class="method-photo" style="left:36px;width:340px;background:linear-gradient(90deg,#3a1c14,#6e3a25 50%,#4a2418)" role="img" aria-label="Judge's gavel in front of law books"></div>
  <div class="method-photo" style="left:428px;width:344px;background:linear-gradient(90deg,#e6e8ec,#c9c2b8 45%,#2b3344)" role="img" aria-label="Business people shaking hands"></div>
  <div class="method-photo" style="left:818px;width:329px;background:linear-gradient(90deg,#0f2a3a,#174560 60%,#d9cfc6)" role="img" aria-label="Hand drawing a rising digital chart line"></div>

  <div class="method-badge" style="left:160px">
    <svg width="44" height="40" viewBox="0 0 44 40" fill="none" stroke="#fff" stroke-width="2.5"><path d="M22 3v30M8 8h28M12 36h20"/><path d="M8 8l-6 14h12zM36 8l-6 14h12z"/><path d="M2 22a6 4 0 0 0 12 0M30 22a6 4 0 0 0 12 0" fill="#fff"/></svg>
  </div>
  <div class="method-badge" style="left:553px">
    <svg width="48" height="30" viewBox="0 0 48 30" fill="#fff"><path d="M2 6l10-4 10 6 6-2 10 2 8 4v8l-8 2-10 8-6-2-8-4-10-6z"/><path d="M18 12l8 5M16 16l8 5M14 20l6 4" stroke="#8c111e" stroke-width="2"/></svg>
  </div>
  <div class="method-badge" style="left:941px">
    <svg width="40" height="44" viewBox="0 0 40 44" fill="none" stroke="#fff" stroke-width="3.5"><circle cx="20" cy="25" r="15"/><path d="M15 4h10M20 4v6"/><path d="M20 25V16" stroke-width="3"/><path d="M20 25l7 6" stroke-width="3"/></svg>
  </div>
</body>
</html>
```